Brochure for Harbor Wellway

A unique, dynamic brochure, our website is: www.harborwellway.example for more information. Our facebook is linked to it to get a sense of who we are. (Please don't use the pictures from there)

Our colors are black, white, and gray. That is our company colors. Open to color though. (If you can have 4 pages on the inside because of too much content, that is fine, or an extra sheet so it has 4 pages inside)

Our mission at Harbor Wellway is to provide love, encourage dreams, and promote integrity. We have a vested interest in Individual and Staff success. We can be reached. (Would like on the first page)

You will have confidence and trust in us.

Harbor Wellway specializes in working with Individuals with Challenging Behaviors and Psychiatric Mental Illness.

Services: Day Services Including: Job Placement including: Supported Employment, Individual Day Supports, Family Supports, Group Day Supports including Group Employment and Group Day Service; Individual Home Supports, Transportation, and Clinical Behavior Supports. (Would like these bulleted)

We provide assessments (Transitional & Life Skills), intense vocation plans including a clinical component which will help the individual to succeed in the job market and beyond.

Harbor Wellway Believes:
Anything is possible for Individuals and has strategies and sound treatment to see this vision forward.
Harbor Wellway’s Chief Executive Officer is A Doctor of Psychology. Her mission is holistic, clinical and fresh.
Harbor Wellway believes in their individuals who they serve and their employees.

Our Holistic Approach views: Employment is viewed as one component of an individual's life that inter-relates with other key aspects, including social relationships, recreation, and where they live. Non-work activities are considered in relationship to employment. Service are provided so that an individual is able to experience all aspects of community life.

The purpose of employment services is not simply to enable a person with a disability to get a job. Providing quality employment support is able people:
(bulleted)
Reaching their fullest potential.
Becoming fully participating community members.
Having a valued role, with all the rights and responsibilities of living in society.
Experiencing and enjoying all that life has to offer.
Redefinining themselves and their place in the world.

A job is simply a vehicle for these things to happen!

Harbor Wellway Employs an Employment Director who is working hand in hand with the community and local business establishments to secure long-term competitive employment for individuals who are served by us. The right job is out there for our individuals to earn money and enhance quality of living. We match the individual with the job that best fits what they want to do for work.

The feel of our program is different. Our individuals served are happy and free to make choices of what their day looks like, participate in schedule development, learn the necessary skills for life and social skills.

And those who are ready to work…WILL WORK. We have over 10 years of experience. We have a motivated team who are unstoppable in our mission. Let us know how we can help you succeed.

A RQB Qualified Provider for the State of Connecticut and MVT Credentialed through PLK.
Approved Provider for the Bureau of Lifelong Care Programs, Spectrum Branch
Private Dollars Accepted as well and Sliding Scale.

Harbor Wellway Corporation
Phone: 555-207-3184
Fax: 555-268-7041
Pending: Non-Profit 501 (c) 3
172 Tamarind Lane
Windsor Locks, CT 06096
www.facebook.com/HarborWellway
www.harborwellway.example
info@harborwellway.example

• The size of the brochure is a booklet brochure. I should definitely post that in the project. The size would be: an 8/12 sheet of paper folded in half.

```html
<!DOCTYPE html>
<html lang="en">
<head>
<meta charset="utf-8">
<title>Harbor Wellway Brochure Spread</title>
<link href="https://fonts.googleapis.com/css2?family=Raleway:wght@300;400&family=Barlow:wght@300;400;500&display=swap" rel="stylesheet">
<style>
  :root {
    --plum: #85275a;
    --plum-text: #8b2d62;
    --ink: #3d3d3d;
    --paper: #ffffff;
    --frame-shadow: rgba(0,0,0,0.28);
  }
  * { margin: 0; padding: 0; box-sizing: border-box; }
  html, body { width: 1200px; height: 927px; overflow: hidden; background: var(--paper); }
  .spread { position: relative; width: 1200px; height: 927px; background: var(--paper); font-family: "Barlow", Arial, sans-serif; color: var(--ink); }

  .headline {
    position: absolute; left: 56px; top: 56px; width: 500px;
    font-family: "Raleway", Arial, sans-serif; font-weight: 300;
    font-size: 24.5px; line-height: 31px; color: var(--plum-text);
  }
  .intro {
    position: absolute; left: 56px; top: 191px; width: 500px;
    font-weight: 300; font-size: 17px; line-height: 22px; letter-spacing: 0.2px;
  }

  .hero { position: absolute; left: 600px; top: 0; width: 600px; height: 256px; }

  .services {
    position: absolute; left: 56px; top: 298px; width: 280px; height: 390px;
    background: var(--plum); color: #fff; text-align: center;
    box-shadow: 2px 3px 6px var(--frame-shadow);
    font-weight: 400; font-size: 15px; line-height: 19.6px; letter-spacing: 0.3px;
  }
  .services h2 { font-weight: 400; font-size: 16.5px; letter-spacing: 0.5px; margin-top: 37px; }
  .services .lead { margin-top: 20px; }
  .services h3 { font-weight: 400; font-size: 16.5px; text-decoration: underline; text-underline-offset: 3px; margin-top: 19px; margin-bottom: 8px; }
  .services ul { list-style: none; }

  .photo {
    position: absolute; background: #fff; padding: 8px;
    box-shadow: 2px 4px 8px var(--frame-shadow);
  }
  .photo-sign { left: 338px; top: 375px; width: 258px; height: 390px; transform: rotate(2.6deg); }
  .photo-wildlife { left: 116px; top: 666px; width: 268px; height: 200px; transform: rotate(-2.4deg); z-index: 2; }
  .photo .fill { width: 100%; height: 100%; }
  .photo-sign .fill { background: linear-gradient(180deg, #d9dde0 0%, #9ea48a 35%, #6f6a4e 60%, #4a3a2e 100%); }
  .photo-wildlife .fill { background: radial-gradient(ellipse at 45% 45%, #5a5a5a 0%, #8c8c8c 45%, #cfcfcf 80%, #e3e3e3 100%); }

  .beliefs { position: absolute; left: 656px; top: 285px; width: 500px; font-weight: 300; font-size: 14.6px; line-height: 19.7px; letter-spacing: 0.15px; }
  .beliefs h2 { font-weight: 500; font-size: 16px; color: var(--plum-text); letter-spacing: 0.4px; margin-bottom: 21px; }
  .beliefs p { margin-bottom: 19.7px; }
  .beliefs h3 { font-weight: 400; font-size: 15px; color: var(--plum-text); }
  .beliefs ul { list-style: none; margin-bottom: 19.7px; font-size: 14px; }
  .beliefs li::before { content: "• "; }
</style>
</head>
<body>
<main class="spread">
  <h1 class="headline">Harbor Wellway specializes in working with Individuals with Challenging Behaviors and Psychiatric Mental Illness.</h1>
  <p class="intro">We provide assessments (Transitional &amp; Life Skills), intense vocation plans including a clinical component which will help the individual to succeed in the job market and beyond.</p>

  <svg class="hero" viewBox="0 0 600 256" role="img" aria-label="Close-up of rainbow coloured leaves covered in water droplets">
    <defs>
      <linearGradient id="heroTones" x1="0" y1="0" x2="1" y2="0">
        <stop offset="0" stop-color="#e8562a"/>
        <stop offset="0.12" stop-color="#a35cc9"/>
        <stop offset="0.3" stop-color="#3a9fd8"/>
        <stop offset="0.45" stop-color="#3fb54a"/>
        <stop offset="0.55" stop-color="#c8d41e"/>
        <stop offset="0.7" stop-color="#f07a28"/>
        <stop offset="0.82" stop-color="#8d63c4"/>
        <stop offset="0.92" stop-color="#e2383e"/>
        <stop offset="1" stop-color="#222"/>
      </linearGradient>
      <linearGradient id="heroShade" x1="0" y1="0" x2="0" y2="1">
        <stop offset="0" stop-color="#000" stop-opacity="0.35"/>
        <stop offset="0.5" stop-color="#000" stop-opacity="0"/>
      </linearGradient>
    </defs>
    <path d="M0 0 H600 V148 C520 150 430 190 340 200 C230 212 120 232 0 256 Z" fill="url(#heroTones)"/>
    <path d="M0 0 H600 V148 C520 150 430 190 340 200 C230 212 120 232 0 256 Z" fill="url(#heroShade)"/>
    <path d="M0 256 C120 232 230 212 340 200 C430 190 520 150 600 148 V172 C520 172 430 205 340 214 C230 226 120 244 0 256 Z" fill="#fff" opacity="0.35"/>
  </svg>

  <section class="services">
    <h2>SERVICES</h2>
    <p class="lead">Day Services Including:</p>
    <h3>Job Placement</h3>
    <ul>
      <li>Supported Employment</li>
      <li>Individual Day Supports</li>
      <li>Family Supports</li>
    </ul>
    <h3>Group Day Supports</h3>
    <ul>
      <li>Group Employment</li>
      <li>Group Day Service</li>
      <li>Individual Home Supports</li>
      <li>Transportation</li>
      <li>Clinical Behavior Supports</li>
    </ul>
  </section>

  <figure class="photo photo-sign"><div class="fill" role="img" aria-label="Office entrance with a roadside sign, shrubs and trees"></div></figure>
  <figure class="photo photo-wildlife"><div class="fill" role="img" aria-label="Black and white photograph of an adult elephant with its calf"></div></figure>

  <section class="beliefs">
    <h2>HARBOR WELLWAY BELIEVES</h2>
    <p>Anything is possible for Individuals and has strategies and sound treatment to see this vision forward. Harbor Wellway’s Chief Executive Officer is a Doctor of Psychology. Her mission is holistic, clinical and fresh. Harbor Wellway believes in their individuals who they serve and their employees.</p>
    <h3>Our Holistic Approach views</h3>
    <p>Employment is viewed as one component of an individual’s life that inter-relates with other key aspects, including social relationships, recreation, and where they live. Non-work activities are considered in relationship to employment. Service are provided so that an individual is able to experience all aspects of community life.</p>
    <p style="margin-bottom:19.7px">The purpose of employment services is not simply to enable a person with a disability to get a job. Providing quality employment support is able people:</p>
    <ul>
      <li>reaching their fullest potential;</li>
      <li>becoming fully participating community members;</li>
      <li>having a valued role, with all the rights and responsibilities of living in society;</li>
      <li>experiencing and enjoying all that life has to offer;</li>
      <li>redefinining themselves and their place in the world.</li>
    </ul>
    <p>The feel of our program is different. Our individuals served are happy and free to make choices of what their day looks like, participate in schedule development, learn the necessary skills for life and social skills.</p>
    <p>And those who are ready to work…WILL WORK. We have over 10 years of experience. We have a motivated team who are unstoppable in our mission. Let us know how we can help you succeed.</p>
  </section>
</main>
</body>
</html>
```